Ice cream packages for CASA MORELLANO

We need a design for ice cream packaging for premium market. Size of the pack 16 oz and 32 oz conic design with cap. Has to be a generic design for all sour flavors, the distinction of the flavors will be don on the stores when people choose the flavor they want and we will place a label of the flavor they close, the design has to be including an area to put the label with the flavor

Target Market(s)

Premium Italian gelato ice cream markets

Industry/Entity Type

Deserts

Font styles to use
Other font styles liked:
• Didot for the logo and brand,

Colors

Designer to choose colors to be used in the design.

Requirements
Must have
• Our design of logo, fonts, and style similar to images sent INCLUD THE FIORE DOLCETTI LOGO , in small size at the side of the container; logo included in the photos bellow
Nice to have
• It has to be an universal design for all flavors, and we need an aérea to place the flavor of the ice cream with a label , expample “chocolate”

```html
<!DOCTYPE html>
<html lang="en">
<head>
<meta charset="utf-8">
<title>Casa Morellano – Gelato Tub Wrap</title>
<link rel="stylesheet" href="https://fonts.googleapis.com/css2?family=Playfair+Display:wght@400;600&family=Montserrat:wght@400;500&display=swap">
<style>
  :root {
    --backdrop: #c9e1f5;
    --wrap-cream: #f1f0ea;
    --wrap-shade: #e4e3dc;
    --lid-band: #ebeae4;
    --brand-pink: #e2187f;
    --tag-grey: #8a8a8a;
    --partner-grey: #6f6f6f;
    --gold-soft: #d8c28c;
    --gold-pale: rgba(216, 194, 140, 0);
    --label-ink: #1e1e1e;
    --label-border: #8d8d8d;
  }
  * { box-sizing: border-box; margin: 0; padding: 0; }
  html, body {
    width: 1200px;
    height: 1200px;
    overflow: hidden;
    background: var(--backdrop);
  }
  .canvas {
    position: relative;
    width: 1200px;
    height: 1200px;
    display: flex;
    align-items: center;
    justify-content: center;
  }
  .tub-wrap {
    position: relative;
    width: 760px;
    height: 980px;
    background: linear-gradient(90deg, var(--wrap-shade) 0%, var(--wrap-cream) 30%, var(--wrap-cream) 70%, var(--wrap-shade) 100%);
    border-radius: 6px;
    overflow: hidden;
  }
  .lid-band {
    position: absolute;
    top: 0; left: 0; right: 0;
    height: 170px;
    background: var(--lid-band);
    border-bottom: 2px solid #dcdbd4;
    display: flex;
    flex-direction: column;
    align-items: center;
    justify-content: center;
  }
  .ornament {
    position: absolute;
    width: 170px;
  }
  .ornament--left  { left: 0;  top: 170px; bottom: 0; background: linear-gradient(90deg, var(--gold-soft), var(--gold-pale)); opacity: .55; }
  .ornament--right { right: 0; top: 0; bottom: 0; background: linear-gradient(270deg, var(--gold-soft), var(--gold-pale)); opacity: .55; }
  .brand-name {
    font-family: "Playfair Display", serif;
    font-weight: 600;
    color: var(--brand-pink);
    line-height: 1;
  }
  .brand-tagline {
    font-family: "Montserrat", sans-serif;
    font-weight: 400;
    color: var(--tag-grey);
    letter-spacing: 0.04em;
    text-transform: uppercase;
  }
  .lid-band .brand-name { font-size: 62px; }
  .lid-band .brand-tagline { font-size: 24px; margin-top: 10px; }
  .partner-mark {
    position: absolute;
    top: 240px;
    left: 50%;
    transform: translateX(-50%);
    width: 260px;
    height: 260px;
    display: flex;
    align-items: center;
    justify-content: center;
  }
  .partner-mark svg { position: absolute; inset: 0; }
  .partner-name {
    position: relative;
    font-family: "Playfair Display", serif;
    font-weight: 400;
    font-size: 34px;
    color: var(--partner-grey);
    text-align: center;
    line-height: 1.15;
  }
  .brand-lockup {
    position: absolute;
    top: 590px;
    left: 0; right: 0;
    display: flex;
    flex-direction: column;
    align-items: center;
  }
  .brand-lockup .brand-name { font-size: 92px; }
  .brand-lockup .brand-tagline { font-size: 32px; margin-top: 14px; }
  .flavor-label {
    position: absolute;
    top: 820px;
    left: 50%;
    transform: translateX(-50%);
    padding: 14px 30px;
    background: #fff;
    border: 2px solid var(--label-border);
    border-radius: 8px;
    font-family: "Playfair Display", serif;
    font-weight: 600;
    font-size: 44px;
    color: var(--label-ink);
  }
</style>
</head>
<body>
  <main class="canvas">
    <section class="tub-wrap">
      <div class="ornament ornament--left" role="img" aria-label="Gold flourish swirl pattern along the left edge"></div>
      <div class="ornament ornament--right" role="img" aria-label="Gold flourish swirl pattern along the right edge"></div>

      <header class="lid-band">
        <p class="brand-name">Casa Morellano</p>
        <p class="brand-tagline">Best gelato in town</p>
      </header>

      <div class="partner-mark">
        <svg viewBox="0 0 260 260" aria-hidden="true">
          <circle cx="130" cy="130" r="118" fill="none" stroke="#8c8c8c" stroke-width="2"/>
        </svg>
        <p class="partner-name">Fiore<br>Dolcetti</p>
      </div>

      <div class="brand-lockup">
        <p class="brand-name">Casa Morellano</p>
        <p class="brand-tagline">Best gelato in town</p>
      </div>

      <p class="flavor-label">Chocolate</p>
    </section>
  </main>
</body>
</html>
```